Business Card Design

Brambique is a floral design company for weddings and special events.
Colours wanted are dark grey, aqua blue, white and black.
dark grey for the background, and the Brambique in the aqua blue, rest of the writing in white and black etc.

Our floral design style is Rustic, textural, natural,
Wanting some kind of simplistic flower symbol next to the Brambique see pictures.

Hi im so sorry I've changed some criteria. been confused on how this site works and what i want!! hope this is more straight forward. I also need clip art of the simple floral design i attached for my web site and also car magnets. thank you thank you thank YOU!!!! cherrs Mel

I have attached x5 ideas on where to place the lotus flower next to and around the brambique. please use simliar colours of the flower as pictured. please cut out the white back ground from the flower. use only petals. use only lotus or the other icon provided per idea. still deciding on which one to use so waiting to see what looks best with your designs. thank you so very much in advance.!! Kindest REgards Mel

hi i am currently getting a logo design made through this also so can we wait until it is complete before any revisions are made. sorry about the delay!! thank you thank you thank you!! kind regards Mel

Reason: im having a logo made also to use on the cards. please hold off on any designs until this is received. thank you and so sorry about this!! cheers mEL

Target Market(s)

modern elegant professional

Industry/Entity Type

Floral

Contact Information for Business Card

Front:
brambique floral design (all lower case) floral design in smaller writting)
www.brambiquefloraldesign.example.au

Back:
Wedding and event design

Melissa - 0490582146
brambique@quillnet.example.au
Petra-0499365017
floristpetralowell@mailbay.example.com

Noosa-Tewantin, Sunshine coast, Qld

Font styles to use
Other font styles liked:
• corben, cookie

Colors
87d0c7
34b8a4
eaf2ce
ffffff
e4daeb
cfdeed

Requirements
Must have
• ; dark grey for back ground. or possible all white?
;brambique floral designs in lower case and in blue' green aqua colour. all other writing in white.
icon which i can also use on the website. see pictures(i want to use the same on my web site.. if you can please make me an clip art icon also?
Nice to have
• simple elegant, earthy, flower icon
or second option icon of lotus looking flower brambique inside
fonts please: brambique floral design in (corben)
all writing on the back in (cookie)
maybe have the same icon clip art provided faintly on the back, bold on the front?
i also need car magnets to
Should not have

```html
<!DOCTYPE html>
<html lang="en">
<head>
<meta charset="utf-8">
<title>Brambique Floral Designers – Business Card</title>
<link rel="stylesheet" href="https://fonts.googleapis.com/css2?family=Cinzel:wght@400;600&family=Open+Sans:wght@400;600;700&display=swap">
<style>
  :root {
    --aqua: #20818c;
    --charcoal: #1f1f20;
    --silver: #a4a4a4;
    --white: #ffffff;
    --backdrop: #dedad4;
  }
  * { margin: 0; padding: 0; box-sizing: border-box; }
  html, body {
    width: 1200px;
    height: 800px;
    overflow: hidden;
    background: var(--backdrop);
    font-family: "Open Sans", sans-serif;
  }
  .stage { position: relative; width: 1200px; height: 800px; }

  /* ---------- Back of card (landscape) ---------- */
  .card-back {
    position: absolute;
    left: 110px;
    top: 255px;
    width: 500px;
    height: 290px;
    background: var(--aqua);
    overflow: hidden;
    box-shadow: 0 6px 18px rgba(0,0,0,0.18);
  }
  .card-back .centre-band {
    position: absolute;
    left: 180px;
    top: 0;
    width: 130px;
    height: 100%;
    background: var(--charcoal);
  }
  .card-back .silver-band {
    position: absolute;
    left: 0;
    top: 230px;
    width: 100%;
    height: 26px;
    background: var(--silver);
  }
  .card-back .aqua-rule {
    position: absolute;
    left: 0;
    top: 222px;
    width: 100%;
    height: 8px;
    background: var(--aqua);
  }
  .card-back .centre-band-lower {
    position: absolute;
    left: 180px;
    top: 214px;
    width: 130px;
    height: 76px;
    background: var(--charcoal);
  }
  .card-back .web-address {
    position: absolute;
    left: 0;
    top: 230px;
    width: 100%;
    height: 26px;
    line-height: 26px;
    text-align: center;
    color: var(--white);
    font-size: 10px;
    letter-spacing: 2.5px;
  }
  .card-back .brand-mark {
    position: absolute;
    left: 180px;
    top: 62px;
    width: 130px;
    display: flex;
    flex-direction: column;
    align-items: center;
    gap: 10px;
  }
  .brand-circle {
    border: 3px solid var(--aqua);
    border-radius: 50%;
  }
  .card-back .brand-circle { width: 76px; height: 76px; }
  .card-back .brand-name {
    font-family: "Cinzel", serif;
    font-weight: 600;
    font-size: 15px;
    letter-spacing: 1px;
    color: var(--aqua);
  }

  /* ---------- Front of card (portrait) ---------- */
  .card-front {
    position: absolute;
    left: 690px;
    top: 150px;
    width: 300px;
    height: 500px;
    background: var(--charcoal);
    overflow: hidden;
    box-shadow: 0 6px 18px rgba(0,0,0,0.18);
  }
  .card-front .silver-edge {
    position: absolute; left: 0; top: 0; width: 14px; height: 100%;
    background: var(--silver);
  }
  .card-front .aqua-edge {
    position: absolute; left: 14px; top: 0; width: 18px; height: 100%;
    background: var(--aqua);
  }
  .card-front .content {
    position: absolute;
    left: 62px;
    top: 96px;
    right: 26px;
  }
  .card-front .brand-circle {
    width: 86px; height: 86px;
    margin-left: 58px;
    margin-bottom: 12px;
  }
  .card-front .brand-name {
    font-family: "Cinzel", serif;
    font-weight: 600;
    font-size: 29px;
    letter-spacing: 1.5px;
    color: var(--aqua);
    line-height: 1;
  }
  .card-front .brand-tagline {
    font-family: "Cinzel", serif;
    font-size: 17px;
    letter-spacing: 1px;
    color: var(--aqua);
    margin-top: 4px;
  }
  .card-front .person {
    margin-top: 26px;
  }
  .card-front .person-name {
    font-weight: 700;
    font-size: 14px;
    letter-spacing: 0.5px;
    text-transform: uppercase;
    color: var(--aqua);
  }
  .card-front .person-role {
    font-size: 13px;
    color: var(--white);
  }
  .contact-list {
    list-style: none;
    margin-top: 22px;
    display: flex;
    flex-direction: column;
    gap: 6px;
  }
  .contact-list li {
    display: flex;
    align-items: center;
    gap: 8px;
    font-size: 10px;
    color: var(--white);
  }
  .contact-list svg { width: 11px; height: 11px; flex: none; fill: var(--aqua); }
</style>
</head>
<body>
<main class="stage">

  <section class="card-back" aria-label="Business card back">
    <div class="aqua-rule"></div>
    <div class="silver-band"></div>
    <div class="centre-band"></div>
    <div class="centre-band-lower"></div>
    <p class="web-address">www.brambiquefloraldesign.example.au</p>
    <div class="brand-mark">
      <div class="brand-circle"></div>
      <span class="brand-name">Brambique</span>
    </div>
  </section>

  <section class="card-front" aria-label="Business card front">
    <div class="silver-edge"></div>
    <div class="aqua-edge"></div>
    <div class="content">
      <div class="brand-circle"></div>
      <h1 class="brand-name">BRAMBIQUE</h1>
      <p class="brand-tagline">Floral Designers</p>

      <div class="person">
        <p class="person-name">Tomas Ferrand</p>
        <p class="person-role">Managing Director</p>
      </div>

      <ul class="contact-list">
        <li>
          <svg viewBox="0 0 12 12" aria-hidden="true"><rect x="3" y="0.5" width="6" height="11" rx="1"/></svg>
          0490 582 146
        </li>
        <li>
          <svg viewBox="0 0 12 12" aria-hidden="true"><path d="M2 1l2.5 0 1 3-1.5 1c.7 1.4 1.6 2.3 3 3l1-1.5 3 1V10c0 .6-.4 1-1 1C5 11 1 7 1 2c0-.6.4-1 1-1z"/></svg>
          0499 365 017
        </li>
        <li>
          <svg viewBox="0 0 12 12" aria-hidden="true"><path d="M0.5 2.5h11v7h-11z M0.5 2.5l5.5 4 5.5-4" fill="none" stroke="#20818c" stroke-width="1.3"/></svg>
          brambique@quillnet.example.au
        </li>
        <li>
          <svg viewBox="0 0 12 12" aria-hidden="true"><circle cx="6" cy="6" r="5.5"/></svg>
          www.brambiquefloraldesign.example.au
        </li>
        <li>
          <svg viewBox="0 0 12 12" aria-hidden="true"><path d="M6 0.5a3.8 3.8 0 0 1 3.8 3.8C9.8 7 6 11.5 6 11.5S2.2 7 2.2 4.3A3.8 3.8 0 0 1 6 .5zm0 2.3a1.5 1.5 0 1 0 0 3 1.5 1.5 0 0 0 0-3z"/></svg>
          14 Reedbank Lane, Noosa-Tewantin QLD
        </li>
      </ul>
    </div>
  </section>

</main>
</body>
</html>
```